Postcard Design

A house cleaning business. Focus on time saving and stress free. Free estimates. Want it to state that we can make your home sparkle or shine. I have been using the colors purple and black in the logo which I will attach.

Reason: I need a few more days to decide on this. Thank you

Industry/Entity Type

House

Colors
886aae
6b449b

Requirements
Must have
• website www.tidwellhavenhomes.us
phone # 555-390-6172

```html
<!DOCTYPE html>
<html lang="en">
<head>
<meta charset="utf-8">
<title>Tidwell Haven Homes – Home Cleaning Flyer</title>
<link rel="stylesheet" href="https://fonts.googleapis.com/css2?family=Montserrat:ital,wght@0,800;1,800&family=Roboto+Condensed:wght@400;700&display=swap">
<style>
  :root{
    --purple:#6b449b;
    --purple-light:#886aae;
    --purple-pale:#a58cc6;
    --black:#1a1a1a;
    --pink:#e6157f;
    --white:#ffffff;
    --backdrop:#5b5b5b;
  }
  *{margin:0;padding:0;box-sizing:border-box}
  html,body{width:962px;height:1200px;overflow:hidden;background:var(--backdrop)}
  .canvas{position:relative;width:962px;height:1200px}
  .flyer{position:absolute;left:83px;top:85px;width:797px;height:1032px;background:var(--white);overflow:hidden}
  .hero{position:absolute;left:0;top:0;width:797px;height:470px}
  .headline{position:absolute;z-index:2;right:26px;top:430px;text-align:right;
    font-family:"Montserrat",sans-serif;font-weight:800;font-size:55px;line-height:61px;color:var(--black);letter-spacing:.5px}
  .tagline{position:absolute;z-index:2;right:24px;top:566px;text-align:right;
    font-family:"Montserrat",sans-serif;font-style:italic;font-weight:800;font-size:22.5px;line-height:32.5px;color:var(--purple-light)}
  .worker-photo{position:absolute;z-index:1;left:6px;top:556px;width:300px;height:314px;
    clip-path:polygon(0 0,74% 0,74% 35%,100% 35%,100% 100%,0 100%);
    background:linear-gradient(160deg,#f1eef4 0%,#d9d4de 50%,#f3e38a 80%,#4a6fb5 100%)}
  .services{position:absolute;left:335px;top:684px;display:grid;grid-template-columns:142px 148px 140px;row-gap:4px;
    font-family:"Roboto Condensed",sans-serif;font-size:22px;line-height:24px;color:var(--black);list-style:none}
  .services li{position:relative;padding-left:19px}
  .services li::before{content:"";position:absolute;left:1px;top:6px;border-left:10px solid var(--pink);border-top:6px solid transparent;border-bottom:6px solid transparent}
  .trust-stamp{position:absolute;z-index:2;left:311px;top:782px;width:209px;height:106px;border:4px solid var(--pink);border-radius:14px;background:var(--white);
    transform:rotate(-3deg);text-align:center;font-family:"Roboto Condensed",sans-serif;font-weight:700;color:var(--pink)}
  .trust-stamp .lead{font-size:19px;margin-top:10px}
  .trust-stamp .big{font-size:30px;line-height:30px;margin-top:4px}
  .brand{position:absolute;left:555px;top:900px;width:220px;text-align:center;
    font-family:"Montserrat",sans-serif;font-weight:800;font-size:24px;line-height:30px;color:var(--purple)}
  .brand-mark{display:block;width:16px;height:16px;border-radius:50%;background:var(--purple);margin:0 auto 10px}
  .phone{position:absolute;left:80px;top:892px;display:flex;align-items:center;gap:6px;
    font-family:"Montserrat",sans-serif;font-weight:800;font-size:45px;color:var(--purple-light)}
  .contact{position:absolute;left:21px;top:950px;display:flex;gap:14px;
    font-family:"Roboto Condensed",sans-serif;font-weight:700;font-size:17.5px;color:var(--purple-light)}
  .contact span::before{content:"";display:inline-block;width:10px;height:10px;background:var(--purple-light);margin-right:7px}
  .cta-band{position:absolute;left:0;bottom:0;width:797px;height:43px;background:var(--purple-light);
    text-align:center;font-family:"Montserrat",sans-serif;font-style:italic;font-weight:800;font-size:26px;line-height:43px;color:var(--white)}
</style>
</head>
<body>
<div class="canvas">
  <section class="flyer">
    <svg class="hero" viewBox="0 0 797 470">
      <defs>
        <linearGradient id="heroBand" x1="0" x2="1">
          <stop offset="0" stop-color="#a58cc6"/><stop offset="1" stop-color="#6b449b"/>
        </linearGradient>
        <linearGradient id="roomTones" x1="0" y1="0" x2="1" y2="1">
          <stop offset="0" stop-color="#f2f2f2"/><stop offset=".6" stop-color="#d9d7d4"/><stop offset="1" stop-color="#6e5a4e"/>
        </linearGradient>
        <linearGradient id="windowTones" x1="0" y1="0" x2="1" y2="1">
          <stop offset="0" stop-color="#9db7d6"/><stop offset="1" stop-color="#e8c93a"/>
        </linearGradient>
        <linearGradient id="floorTones" x1="0" y1="0" x2="0" y2="1">
          <stop offset="0" stop-color="#eeeeee"/><stop offset="1" stop-color="#c9814a"/>
        </linearGradient>
      </defs>
      <rect width="797" height="470" fill="var(--white)"/>
      <rect width="797" height="140" fill="url(#heroBand)"/>
      <path d="M0 0 H430 Q520 30 560 75 Q300 20 0 35 Z" fill="var(--black)"/>
      <path d="M0 42 Q300 30 565 90" stroke="var(--white)" stroke-width="3" fill="none"/>
      <rect x="0" y="130" width="640" height="330" fill="url(#roomTones)" role="img" aria-label="Photo of a bright, clean modern living and dining room"/>
      <path d="M0 415 Q400 360 797 372 V400 Q400 395 0 465 Z" fill="url(#heroBand)"/>
      <path d="M0 465 Q400 395 797 400 V470 H0 Z" fill="var(--white)"/>
      <circle cx="527" cy="127" r="102" fill="url(#windowTones)" stroke="var(--white)" stroke-width="8" role="img" aria-label="Photo of a gloved hand washing a window with a sponge"/>
      <circle cx="697" cy="240" r="117" fill="url(#floorTones)" stroke="var(--white)" stroke-width="8" role="img" aria-label="Photo of a person mopping a wooden floor beside a bucket"/>
    </svg>

    <h1 class="headline">WE MAKE YOUR<br>HOME SPARKLE !!</h1>
    <p class="tagline">TIDWELL HAVEN HOMES<br>OFFERS OLD FASHION, HIGH-QUALITY<br>HOME CLEANING SERVICES.</p>

    <div class="worker-photo" role="img" aria-label="Photo of a smiling cleaner in white overalls mopping beside a cleaning cart"></div>

    <ul class="services">
      <li>Mop/Sweep</li><li>Wash Walls</li><li>Windows</li>
      <li>Vaccum</li><li>Baseboards</li><li>Dusting</li>
      <li>Bathrooms</li><li>Blinds</li><li>Much More!</li>
    </ul>

    <div class="trust-stamp">
      <p class="lead">Our professionals are</p>
      <p class="big">INSURED<br>AND BONDED</p>
    </div>

    <div class="brand"><span class="brand-mark"></span>Tidwell Haven Homes</div>

    <div class="phone">
      <svg width="40" height="40" viewBox="0 0 40 40" aria-hidden="true">
        <circle cx="20" cy="20" r="17" fill="none" stroke="var(--purple-light)" stroke-width="3.5"/>
        <path d="M15 10 q-5 10 0 20 l4-3 q-3-7 0-14 z" fill="var(--purple-light)"/>
      </svg>
      <span>555-390-6172</span>
    </div>

    <p class="contact"><span>www.tidwellhavenhomes.us</span><span>hello@tidwellhavenhomes.us</span></p>

    <p class="cta-band">CALL TODAY FOR A FREE ESTIMATE!</p>
  </section>
</div>
</body>
</html>
```